Amber Reed Catering Menu

Design 1 page (double sided is ok) menu for catering company.

A flat non-folding menu. Letter paper sized.
Updates

I'm having trouble adding attachments via Pixel Forum.  I have contacted Pixel Forum and will hopefully have them up soon.  

Industry/Entity Type

Catering

Font styles to use
Serif

Requirements
Must have
• Amber Reed Catering logo

menu items from attachment

Double sided is ok

```html
<!DOCTYPE html>
<html lang="en">
<head>
<meta charset="utf-8">
<title>Amber Reed Catering Menu</title>
<link rel="stylesheet" href="https://fonts.googleapis.com/css2?family=Cinzel:wght@400;600&family=Crimson+Text:wght@400;700&display=swap">
<style>
  :root {
    --paper: #f5f5f5;
    --brand-blue: #3f74b5;
    --band-blue: #3a70b2;
    --leaf-green: #3b6d12;
    --rule-light: #a9c3e0;
  }
  * { margin: 0; padding: 0; box-sizing: border-box; }
  html, body { width: 927px; height: 1200px; overflow: hidden; background: var(--paper); }
  .menu-page { position: relative; width: 927px; height: 1200px; background: var(--paper); }

  .brand-name {
    position: absolute; top: 68px; left: 0; width: 927px; text-align: center;
    font-family: "Cinzel", serif; font-weight: 600; font-size: 32px;
    color: var(--brand-blue); letter-spacing: 0.5px;
  }

  .band {
    position: absolute; left: 0; width: 900px; height: 7px;
    background: linear-gradient(90deg, var(--band-blue) 0%, var(--band-blue) 35%, rgba(169,195,224,0.6) 75%, rgba(245,245,245,0) 100%);
  }
  .band--thin { height: 6px; }
  .band-tick { position: absolute; left: 0; width: 4px; height: 6px; background: var(--band-blue); }

  .intro {
    position: absolute; top: 178px; left: 0; width: 927px; text-align: center;
    font-family: "Cinzel", serif; font-size: 20px; color: var(--brand-blue); line-height: 20px;
  }
  .intro p { margin: 0; }
  .intro .gap { height: 20px; }

  .menu-section { position: absolute; left: 93px; }
  .menu-section__title {
    font-family: "Cinzel", serif; font-size: 22px; color: var(--brand-blue);
    letter-spacing: 0.5px; line-height: 26px; margin-bottom: 8px;
  }
  .menu-item { margin-left: 34px; margin-bottom: 18px; font-family: "Crimson Text", serif; font-size: 19px; line-height: 18px; }
  .menu-item__name { color: var(--brand-blue); font-weight: 700; }
  .menu-item__line { color: var(--leaf-green); }

  .contact-bar {
    position: absolute; top: 1124px; left: 0; width: 927px; text-align: center;
    font-family: "Cinzel", serif; font-size: 22px; color: var(--brand-blue); word-spacing: 1px;
  }
  .contact-bar .divider { margin: 0 22px; }
</style>
</head>
<body>
<main class="menu-page">
  <div class="brand-name">Amber Reed Catering</div>

  <div class="band" style="top:155px"></div>

  <section class="intro">
    <p>Catering Director: Dana Whitlock</p>
    <p>Phone: 555-210-4817</p>
    <p>Fax: 555-210-4820</p>
    <p>Cell: 555-390-6254</p>
    <div class="gap"></div>
    <p>Caterings for all occasions</p>
    <div class="gap"></div>
    <p>Enjoy our pre-set menu or</p>
    <div class="gap"></div>
    <p>we can customize something more personal.</p>
    <p>Set up and delivery is included in all prices listed.</p>
  </section>

  <div class="band" style="top:418px"></div>
  <div class="band band--thin" style="top:434px"></div>

  <section class="menu-section" style="top:452px">
    <h2 class="menu-section__title">Breakfast Menu</h2>
    <div class="menu-item">
      <div class="menu-item__name">Morning Stretch $5.99 per guest</div>
      <div class="menu-item__line">Assorted Danishes, Muffins, Bagels with Cream Cheese, Butter, Jelly</div>
      <div class="menu-item__line">Fresh Brewed Coffee, Decaf and Assorted Teas</div>
    </div>
    <div class="menu-item">
      <div class="menu-item__name">Healthy Start $6.99 per guest</div>
      <div class="menu-item__line">Fresh Fruit, Assorted Muffins or Bagels with Cream Cheese, Jelly, and Butter</div>
      <div class="menu-item__line">Orange Juice</div>
      <div class="menu-item__line">Fresh Brewed Coffee, Decaf and Assorted Teas</div>
    </div>
    <div class="menu-item">
      <div class="menu-item__name">Breakfast Sandwich $7.99 per guest</div>
      <div class="menu-item__line">Bagel, Biscuit or Wrap with Egg and Cheese and choice of: Bacon, Sausage or Ham</div>
      <div class="menu-item__line">Orange Juice</div>
      <div class="menu-item__line">Fresh Brewed Coffee Decaf and Assorted Teas</div>
    </div>
    <div class="menu-item">
      <div class="menu-item__name">Grand Deluxe $8.99 per guest</div>
      <div class="menu-item__line">Fresh Scrambled Eggs, Bacon, Home Fries, Bread</div>
      <div class="menu-item__line">Orange Juice</div>
      <div class="menu-item__line">Fresh Brewed Coffee, Decaf and Assorted Tea</div>
    </div>
  </section>

  <div class="band" style="top:837px"></div>
  <div class="band-tick" style="top:852px"></div>

  <section class="menu-section" style="top:863px">
    <h2 class="menu-section__title">Lunch Menu</h2>
    <div class="menu-item">
      <div class="menu-item__name">Boxed Lunch $7.99 per guest</div>
      <div class="menu-item__line">Sandwich or Wrap with choice of: Assorted Chips, Pasta Salad, or Potato Salad</div>
      <div class="menu-item__line">Brownie or Cookie</div>
      <div class="menu-item__line">Can Soda or Bottle Water</div>
    </div>
    <div class="menu-item">
      <div class="menu-item__name">Cold Cut Platter $9.99 per guest</div>
      <div class="menu-item__line">Assorted Meats (Turkey, Ham, Roast Beef) and Cheeses with varying Breads</div>
      <div class="menu-item__line">Choice of: Potato Salad, Pasta Salad, Coleslaw, or Chips</div>
      <div class="menu-item__line">Cookie or Brownie</div>
      <div class="menu-item__line">Can Soda or Bottle Water</div>
    </div>
  </section>

  <div class="band" style="top:1098px"></div>
  <div class="band-tick" style="top:1133px"></div>

  <footer class="contact-bar">
    Phone: 555-210-4817<span class="divider">|</span>Fax: 555-210-4820<span class="divider">|</span>Cell: 555-390-6254
  </footer>
</main>
</body>
</html>
```